Buchcover-Design für Detoxkur
Vielen lieben Dank für die professionelle Zusammenarbeit, die sich auch im zweiten Projekt erfolgreich bestätigen ließ. Tip Top! Dankeschön!!!!
Zielgruppe
Ich bin Gesundheits- und Ernährungsberater und suche nach einem Buchcover für mein neues Projekt (Taschenbuch und E-Book) Meine Zielgruppe sind Menschen die auf der Suche nach Heilung und mehr Wohlbefinden sind. (Detoxkur-Entschlacken und Entgiften etc....)
Aufgabenstellung
Das Design sollte durch den Titel deutlich auffallen. Vorzugsweise ein dunkler Hintergrund, Titel in großer Schrift. Eingearbeitet etwas Gemüse und Obst, grüner Saft oder auch ein Smoothie, Zitronenwasser, Magen- und Darmtrakt oder ähnlichem. Es darf auch verspielt sein aber dennoch Niveauvoll.
Das Buch einschließlich Titel und Untertitel, sowie Klappentext werden derzeit von einem Lektor bearbeitet, also können diesbezüglich noch leichte Änderungen anfallen die dann anzupassen wären.
Das Buchformat ist 12cm x 19cm. Die Endgültigen Abmaße müssten nach dem Buchindesign noch angepasst werden, wenn die Seitenzahlen feststehen.
Würde gerne den Coverdesigner im Impressum des Buchs erwähnen und Bitte darum um Einverständnis, wenn es auch erwünscht sein sollte!
Derzeitiger Text :
Titel: Morgenlicht - Finde Ruhe durch Wandern und Tagträumen
Untertitel: - Durch Entgiften und Entschlacken das Wohlbefinden steigern, die Darmgesundheit wieder herstellen, das Gewicht reduzieren und die Heilung für Körper und Geist einleiten -
Klappentext: Bist du auf der Suche nach mehr Wohlbefinden und möchtest deine Gesundheit nachhaltig verbessern? Suchst du nach Methoden deinen Körper von Schadstoffen zu befreien, die dich in der Vergangenheit belastet haben? Möglicherweise fragst du dich warum das so ist und was es damit auf sich hat?
Detox, Entschlacken und Entgiften, Diäten und eine gesündere Ernährungsweise ist in aller Munde. Der Grund dafür ist bei zahlreichen Menschen ein mangelndes Wohlbefinden durch zivillisationsbedingte Einflüsse wie Umweltverschmutzungen, Stress und eine unbewusste Ernährungsweise. Diese Faktoren führen zu krankhaften Symptomen, Energie- und Antriebslosigkeit und letztendlich zu den steigenden Zahlen übergewichtiger Menschen in unserer Bevölkerung.
In diesem Ratgeber erfährst du, wie wichtig es ist sich zu entgiften und wie wichtig dafür eine gesunde Ernähru..

```html
<!DOCTYPE html>
<html lang="de">
<head>
<meta charset="utf-8">
<title>Morgenlicht – Buchcover</title>
<link href="https://fonts.googleapis.com/css2?family=Bungee&family=Roboto:wght@400;700&family=Roboto+Condensed:wght@300;400&display=swap" rel="stylesheet">
<style>
  :root {
    --green: #7dc20f;
    --dark: #0d1a1f;
    --ink: #1b1f22;
    --paper: #f4f5f5;
    --light-text: #d9dee1;
    --white: #ffffff;
  }
  html, body { margin: 0; padding: 0; overflow: hidden; background: var(--white); }
  .cover {
    position: relative;
    width: 1200px;
    height: 896px;
    overflow: hidden;
    font-family: "Roboto", sans-serif;
  }

  /* Back cover */
  .back {
    position: absolute; left: 0; top: 0; width: 553px; height: 896px;
    background: linear-gradient(180deg, #ffffff 0%, var(--paper) 40%, #eeefef 100%);
  }
  .back-title {
    position: absolute; left: 0; top: 100px; width: 540px; margin: 0;
    text-align: center; font-family: "Bungee", sans-serif; font-weight: 400;
    font-size: 46px; line-height: 64px; color: var(--green); letter-spacing: 1px;
  }
  .back-subtitle {
    position: absolute; left: 0; top: 172px; width: 540px; margin: 0;
    text-align: center; font-weight: 700; font-size: 24px; line-height: 30px;
    color: var(--ink); letter-spacing: 0.5px; text-transform: uppercase;
  }
  .blurb {
    position: absolute; left: 30px; top: 248px; width: 495px;
    font-size: 15.3px; line-height: 19.5px; color: var(--ink); letter-spacing: 0.4px;
  }
  .blurb p { margin: 0 0 19.5px; }
  .back-produce {
    position: absolute; left: 0; top: 757px; width: 553px; height: 139px;
    background: linear-gradient(90deg, #7a9c4a 0%, #c9d9a0 20%, #e8c24a 45%, #d8743a 65%, #b8d06a 80%, #c6452f 100%);
    -webkit-mask-image: linear-gradient(180deg, transparent 0%, #000 40%);
            mask-image: linear-gradient(180deg, transparent 0%, #000 40%);
  }

  /* Spine */
  .spine {
    position: absolute; left: 553px; top: 0; width: 94px; height: 896px;
    background: var(--dark);
  }
  .spine-text {
    position: absolute; left: 47px; top: 458px;
    transform: translate(-50%, -50%) rotate(-90deg);
    white-space: nowrap; font-size: 15.5px; letter-spacing: 0.6px;
  }
  .spine-author { color: var(--white); }
  .spine-title { color: var(--green); }

  /* Front cover */
  .front {
    position: absolute; left: 647px; top: 0; width: 553px; height: 896px;
    background: #ffffff;
  }
  .front-author {
    position: absolute; left: 0; top: 50px; width: 553px; margin: 0;
    text-align: center; font-size: 30px; font-weight: 400; color: var(--ink);
    letter-spacing: 1px; line-height: 36px;
  }
  .front-produce {
    position: absolute; left: 0; top: 100px; width: 553px; height: 700px;
    background: radial-gradient(ellipse at 50% 50%, #ffffff 0%, #ffffff 38%, rgba(255,255,255,0) 60%),
                linear-gradient(160deg, #d8372a 0%, #9cc43c 25%, #f0a33a 45%, #e4352b 60%, #3f7a2c 80%, #6ba33a 100%);
  }
  .title-panel {
    position: absolute; left: 90px; top: 196px; width: 378px; height: 458px;
    background: var(--dark);
  }
  .front-title {
    position: absolute; left: 25px; top: 40px; margin: 0;
    font-family: "Bungee", sans-serif; font-weight: 400;
    font-size: 39px; line-height: 72px; color: var(--green);
  }
  .front-subtitle {
    position: absolute; left: 25px; top: 118px; margin: 0; width: 340px;
    font-family: "Roboto Condensed", sans-serif; font-weight: 400;
    font-size: 40px; line-height: 49px; color: var(--light-text); text-transform: uppercase;
  }
  .tagline-band {
    position: absolute; left: 0; top: 799px; width: 553px; height: 97px;
    background: var(--green);
  }
  .tagline {
    position: absolute; left: 24px; top: 13px; width: 520px; margin: 0;
    font-family: "Roboto Condensed", sans-serif; font-weight: 400;
    font-size: 19px; line-height: 24.5px; color: var(--white);
  }
</style>
</head>
<body>
<div class="cover">

  <section class="back">
    <h2 class="back-title">MORGENLICHT</h2>
    <p class="back-subtitle">Finde Ruhe durch Wandern<br>und Tagträumen</p>
    <div class="blurb">
      <p>Bist du auf der Suche nach mehr Wohlbefinden und möchtest deine Gesundheit nachhaltig verbessern? Suchst du nach Methoden deinen Körper von Schadstoffen zu befreien, die dich in der Vergangenheit belastet haben? Möglicherweise fragst du dich warum das so ist und was es damit auf sich hat?</p>
      <p>Detox, Entschlacken und Entgiften, Diäten und eine gesündere Ernährungsweise ist in aller Munde. Der Grund dafür ist bei zahlreichen Menschen ein mangelndes Wohlbefinden durch zivillisationsbedingte Einflüsse wie Umweltverschmutzungen, Stress und eine unbewusste Ernährungsweise. Diese Faktoren führen zu krankhaften Symptomen, Energie- und Antriebs&shy;losigkeit und letztendlich zu den steigenden Zahlen überge&shy;wichtiger Menschen in unserer Bevölkerung.</p>
      <p>In diesem Ratgeber erfährst du, wie wichtig es ist sich zu entgiften und wie wichtig dafür eine gesunde Ernährungs&shy;weise ist. Zusätzlich erfährst du, wie du praktische Heil&shy;methoden anwendest, die die Darmgesundheit wiederherstellen und wie du die Entgiftung in den einzelnen Bereichen des Körpers vorantreibst. Denn Detox ist heutzutage wichtiger denn je!</p>
    </div>
    <div class="back-produce" role="img" aria-label="Foto einer Reihe frischer Gemüsesorten: Kohl, Spargel, Mais, Blumenkohl, Paprika, Karotten und Tomaten"></div>
  </section>

  <section class="spine">
    <div class="spine-text">
      <span class="spine-author">LUKAS WENDRICH</span>
      <span class="spine-title">&nbsp;- MORGENLICHT - FINDE RUHE DURCH WANDERN UND TAGTRÄUMEN</span>
    </div>
  </section>

  <section class="front">
    <p class="front-author">LUKAS WENDRICH</p>
    <div class="front-produce" role="img" aria-label="Foto eines Rahmens aus frischem Obst und Gemüse: Tomaten, Paprika, Erdbeeren, Zitrone, Äpfel, Kiwi, Gurke, Brokkoli und Kräuter auf weißem Grund"></div>
    <div class="title-panel">
      <h1 class="front-title">MORGENLICHT</h1>
      <p class="front-subtitle">Finde Ruhe durch Wandern und Tagträumen</p>
    </div>
    <div class="tagline-band">
      <p class="tagline">Durch Entgiften und Entschlacken das Wohlbefinden steigern, die Darmgesundheit wieder herstellen, das Gewicht reduzieren und die Heilung für Körper und Geist einleiten</p>
    </div>
  </section>

</div>
</body>
</html>
```